Dental Patient Education Single page-Multiple pages needed.

I am creating a unique dental patient education materials for resale. I work in the dental industry, training dentists and thier teams how to improve patient acceptance rates for treatment. I see a need that all patient education material is designed incorrectly. I want to fix this by creating patient education material that educated patients based on all of the treatment options for a diagnosed condition. Tradidional patient education material reads like a catalog of procedures. This format is not effective for helping the patient quickly understand the consequences of non treatment and the benefits and disadvantages of their treatment options. Specifics of the Job:The design images must be royalty free.I will provide the text.Initially there are for major diagnosed conditions: Infected Tooth Treatment Options, Single to Multiple Missing tooth Treatment Options, Full Arch of Missing Teeth Treatment Options, and Full Arch Fixed Dental Implant Treatment OptionsThe layout should mirror the attached sample of Single Missing Tooth Treatment Options.This is a project that will require edits and redesigned based on testing.I also need this in Adobe, so it can be customized/branded for a dental office.

Target Market(s)

Dental office professionals to educate patients.

Font styles to use
Sans Serif

Colors
3277b5

Requirements
Must have
• Professional look and feel
• Royalty free images
• Easy to read

```html
<!DOCTYPE html>
<html lang="en">
<head>
<meta charset="utf-8">
<title>Single Missing Tooth – Treatment Options</title>
<link href="https://fonts.googleapis.com/css2?family=Montserrat:wght@400;500;600;700;800&display=swap" rel="stylesheet">
<style>
:root{
  --brand:#3277b5;
  --brand-deep:#1f5f9e;
  --navy:#0f1f3a;
  --ink:#2b2b2e;
  --panel:#e6e8ec;
  --stage:#eceef1;
  --white:#ffffff;
}
*{margin:0;padding:0;box-sizing:border-box}
html,body{width:1200px;height:859px;overflow:hidden;background:var(--stage);font-family:'Montserrat',sans-serif;color:var(--ink)}
.spread{position:relative;width:1200px;height:859px}
.page{position:absolute;top:62px;width:519px;height:734px;background:var(--white);overflow:hidden}
.page--cover{left:62px}
.page--options{left:618px}
.page svg.art{position:absolute;left:0;top:0}
.cover-title{position:absolute;left:32px;top:458px;font-weight:800;font-size:47px;line-height:51px;color:var(--brand);letter-spacing:.5px}
.cover-band{position:absolute;left:0;top:568px;width:474px;height:23px;background:var(--brand);clip-path:polygon(0 0,100% 0,96% 100%,0 100%)}
.cover-band span{display:block;padding-left:32px;line-height:23px;font-size:14px;font-weight:500;color:var(--white)}
.cover-intro{position:absolute;left:32px;top:604px;width:310px;font-size:10.2px;font-weight:500;line-height:12.6px;white-space:nowrap}
.cover-intro p+p{margin-top:11px}
.options-panel{position:absolute;left:294px;top:0;width:225px;height:734px;background:var(--panel)}
.figure{position:absolute;border-radius:2px}
.option{position:absolute;left:32px;width:251px}
.option h2{font-size:16.5px;font-weight:700;line-height:21px;color:var(--brand);text-transform:uppercase}
.option p{margin-top:12px;font-size:9.2px;line-height:11.6px;text-align:justify;color:#3a3a3d}
</style>
</head>
<body>
<div class="spread">

  <section class="page page--cover">
    <svg class="art" width="519" height="734" viewBox="0 0 519 734">
      <defs>
        <linearGradient id="photoTone" x1="0" y1="0" x2="1" y2="1">
          <stop offset="0" stop-color="#9fc3e0"/>
          <stop offset=".55" stop-color="#e9d6cc"/>
          <stop offset="1" stop-color="#5a8fc2"/>
        </linearGradient>
        <linearGradient id="swoosh" x1="0" y1="0" x2="1" y2="1">
          <stop offset="0" stop-color="#1f5f9e"/>
          <stop offset="1" stop-color="#3277b5"/>
        </linearGradient>
      </defs>
      <path d="M6 0 H40 C100 300 300 455 519 470 V492 C290 485 60 330 6 0 Z" fill="url(#swoosh)"/>
      <path d="M40 0 C110 300 300 455 519 470 V478 C300 470 95 320 28 0 Z" fill="#d7dbe1"/>
      <path d="M42 0 H519 V470 C330 455 120 330 42 0 Z" fill="url(#photoTone)" role="img" aria-label="Photo of a smiling patient in a dental chair while a dentist examines her teeth with a mirror and probe"/>
      <path d="M0 734 V718 C200 714 410 676 519 624 V734 Z" fill="var(--brand)"/>
      <path d="M0 734 V726 C210 724 410 696 519 652 V734 Z" fill="var(--navy)"/>
      <path d="M0 734 V731 C220 730 410 712 519 676 V734 Z" fill="var(--brand-deep)"/>
    </svg>
    <h1 class="cover-title">SINGLE<br>MISSING TOOTH</h1>
    <div class="cover-band"><span>A missing tooth is a serious issue. It can cause long-term</span></div>
    <div class="cover-intro">
      <p>A missing tooth is a serious issue. It can cause long-term<br>damage to facial structure, bone density and your<br>ability to feel confident in your smile.</p>
      <p>Brightwell Dental Studio has several options<br>available to fix your missing tooth.</p>
    </div>
  </section>

  <section class="page page--options">
    <div class="options-panel"></div>
    <div class="figure" style="left:327px;top:52px;width:158px;height:116px;background:linear-gradient(135deg,#27313a,#7d8a94 60%,#2c353d)" role="img" aria-label="Dental X-ray showing the gap left by a missing tooth"></div>
    <div class="figure" style="left:302px;top:246px;width:204px;height:112px;background:linear-gradient(180deg,#e7b9b6,#f4f1ee 60%,#e6e8ec)" role="img" aria-label="Illustration of a dental implant with labelled implant, abutment and crown"></div>
    <div class="figure" style="left:310px;top:414px;width:201px;height:116px;background:linear-gradient(180deg,#dca3a3,#f6f4f1 55%,#e6e8ec)" role="img" aria-label="Illustration of a three-unit dental bridge fitting over two prepared teeth"></div>
    <div class="figure" style="left:310px;top:550px;width:201px;height:120px;background:linear-gradient(180deg,#dca3a3,#f6f4f1 45%,#d98f8f)" role="img" aria-label="Illustration of a removable partial denture with clasps"></div>
    <svg class="art" width="519" height="734" viewBox="0 0 519 734">
      <path d="M0 734 V726 C180 722 380 700 519 654 V734 Z" fill="var(--brand)"/>
      <path d="M0 734 V730 C200 728 390 712 519 678 V734 Z" fill="var(--navy)"/>
    </svg>

    <article class="option" style="top:54px">
      <h2>Option 1:<br>Do Nothing</h2>
      <p>If you choose to do nothing at this time, the cost down the road can be substantial. $10,000+ for orthodontics to straighten out the teeth, implant, abutment and crown, bone grafting and possible sinus lift to replace lost bone.</p>
    </article>
    <article class="option" style="top:177px">
      <h2>Option 2:<br>Dental Implant</h2>
      <p>The bad news is that a dental implant is the most expensive option, BUT the good news is it is the most effective, functional and aesthetically pleasing. A dental implant will keep the bone in that area of the jaw from atrophy. It helps maintain face shape and prevents 'sunken face'. The implant will prevent surrounding teeth from shifting and chances of losing the tooth decline. It will keep the teeth from shifting, and will prevent any future need to cut down the adjacent teeth. A dental implant is the nearest thing to a natural tooth available today.</p>
    </article>
    <article class="option" style="top:369px">
      <h2>Option 3:<br>Dental Bridge</h2>
      <p>The good news here is that a bridge is less expensive than the implant option BUT you will continue to lose bone in that area over time. Food will get caught in the hard to reach areas and if not cleaned properly could mean you have to replace the bridge every 7 years. In addition, to secure the bridge, the adjacent teeth must be cut down in order to be used as anchors for the appliance. Why cut down two good teeth if we don't have to?</p>
    </article>
    <article class="option" style="top:539px">
      <h2>Option 4:<br>The Removable Partial<br>Denture (RPD)</h2>
      <p>The good news here is that it's the least expensive option of the 3, but the BAD news is that your teeth have to come out every night. You won't be able to chew your food as well and your tongue will be uncomfortable with the big, bulky plastic sitting in your mouth all day.</p>
    </article>
  </section>

</div>
</body>
</html>
```